Quellmont Haus National Website

We need a website to match our Logo. We will be selling american made vapeing Oils, batteries, Cartomizers, Clearomizers. We have a wharehouse location with couches, TVs streaming clipora, vending machine, and the worlds first flavor mixing bar. We have the lowest priced high grade oils. We will send pictures of the location. Relaxed atmoshpere and no lines for purchase. VIP cards for regulars.

(PLEASE KNOW THAT THE LOGO IS THE UPPER RIGHT LOGO ONLY OF THE FOUR ON THE FILE I ATTACHED)
Updates

Keep in mind we are are only looking for concept and a non coded website

Please know that we are looking for a non coded website

Industry/Entity Type

Purchase

Requirements
Must have
• Online cart, Blog,

```html
<!DOCTYPE html>
<html lang="en">
<head>
<meta charset="utf-8">
<title>Quellmont Haus — Blog</title>
<link href="https://fonts.googleapis.com/css2?family=Josefin+Sans:wght@300;400;600;700&display=swap" rel="stylesheet">
<style>
:root{
  --black:#111111;
  --ink:#222222;
  --green:#7cc242;
  --green-dark:#5e9e2c;
  --green-pale:#c9e6a6;
  --green-soft:#b6dc8a;
  --page:#ececec;
  --white:#ffffff;
  --muted:#8a8a8a;
  --footer-text:#bdbdbd;
}
*{box-sizing:border-box;margin:0;padding:0}
html,body{width:775px;height:1200px;overflow:hidden}
body{position:relative;background:var(--page);font-family:"Josefin Sans",Arial,sans-serif;color:var(--ink)}
.abs{position:absolute}

/* header */
.site-header{left:0;top:0;width:775px;height:47px;background:var(--black)}
.brand{color:var(--white);font-weight:400;font-size:25px;display:flex;align-items:center;gap:7px}
.brand .mark{width:9px;height:9px;background:var(--green)}
.site-header .brand{left:24px;top:10px}
.main-nav{right:168px;top:32px;display:flex;gap:18px;font-size:8px;color:var(--white)}
.main-nav .current{border-bottom:2px solid var(--white);padding-bottom:2px}
.auth{right:20px;top:26px;display:flex;gap:6px}
.auth span{font-size:8px;font-weight:700;padding:4px 9px;color:var(--white)}
.auth .login{background:var(--green)}
.auth .signup{background:#3a3a3a}

/* tool bar */
.toolbar{left:0;top:47px;width:775px;height:42px;background:linear-gradient(var(--green),var(--green-dark))}
.discuss{left:29px;top:8px;width:78px;height:26px;background:var(--black);color:var(--white);font-size:7px;display:flex;align-items:center;gap:6px;padding-left:5px;line-height:9px}
.discuss .bubble{width:16px;height:14px;background:var(--white);border-radius:50%}
.search{left:244px;top:9px;height:22px;display:flex}
.search .label{background:var(--black);color:var(--white);font-size:9px;font-weight:700;width:67px;display:flex;align-items:center;justify-content:center}
.search .field{background:var(--white);width:232px;font-size:7px;color:var(--muted);display:flex;align-items:center;padding-left:8px}
.search .go{background:var(--green);color:var(--white);font-size:9px;font-weight:700;width:38px;display:flex;align-items:center;justify-content:center;margin-left:2px}

/* sidebar */
.sidebar{left:643px;top:89px;width:132px;height:894px;background:var(--green-soft)}
.side-head{left:643px;width:132px;color:var(--white);font-size:10px;letter-spacing:.5px;display:flex;align-items:center;gap:8px}
.side-head .arrow{width:14px;height:14px;border:1.5px solid var(--white);border-radius:50%;display:inline-flex;align-items:center;justify-content:center;font-size:8px}
.cat-head{top:47px;height:42px;padding-left:14px;border-left:1px solid #9bd36c}
.categories{left:643px;top:89px;width:123px;height:244px;background:var(--green-pale);padding:8px 0 0 24px}
.categories .group{border-bottom:1px solid var(--green-dark);padding:2px 0 4px;width:88px;margin-bottom:4px}
.categories .group:last-child{border-bottom:none}
.categories h4{font-weight:400;font-size:10px;line-height:12px;color:var(--black)}
.categories li{list-style:none;font-size:7px;margin-left:6px;line-height:8px}
.categories li::before{content:"• "}
.scroll{left:764px;top:95px;width:5px;height:30px;background:var(--green-dark)}
.gallery-head{top:333px;height:47px;background:var(--green-dark);padding-left:14px}
.gallery{left:655px;top:397px;width:110px;display:grid;grid-template-columns:48px 48px;gap:12px 9px}
.gallery .thumb{width:48px;height:48px;border:2px solid var(--white)}
.divider-black{left:643px;top:573px;width:132px;height:5px;background:var(--black)}
.events-head{top:580px;height:40px;background:var(--green-dark);justify-content:flex-end;padding-right:16px}
.event-art{left:656px;top:629px;width:106px;height:262px;background:linear-gradient(160deg,#f3e7c9,#d97a2b 45%,#8a5a2a 70%,#f3e7c9);border:3px solid #f6efdc}

/* posts */
.welcome{left:71px;top:104px;font-weight:300;font-size:17px;letter-spacing:1px;color:var(--black)}
.welcome-sub{left:240px;top:124px;font-size:5px;color:var(--muted)}
.post-icon{left:64px;width:44px;height:36px;background:var(--green);display:flex;align-items:center;justify-content:center}
.post-title{left:120px;width:510px;height:34px;background:var(--black);color:var(--white);font-size:11px;font-weight:400;display:flex;align-items:center;padding-left:18px;letter-spacing:.5px}
.post-meta{left:64px;width:44px;background:var(--white);font-size:6px;text-align:right;padding:6px 3px;line-height:7px;white-space:nowrap}
.post-meta .date{color:var(--green-dark);font-size:9px}
.post-meta .date b{font-size:14px;font-weight:400}
.post-meta .tags{color:var(--green-dark);font-size:4px;line-height:5px}
.photo{background:linear-gradient(135deg,#3a3a3a,#111 70%)}
.post-text{font-size:7.4px;line-height:10.7px;color:var(--black)}
.actions{display:flex;gap:6px}
.actions .act{width:24px;text-align:center;font-size:5px}
.actions .btn{width:24px;height:20px;background:var(--green);display:flex;align-items:center;justify-content:center;margin-bottom:2px}
.rule{left:112px;width:520px;height:4px;background:var(--green-soft)}
.video{left:177px;top:816px;width:394px;height:167px;background:linear-gradient(180deg,#6d6259,#cbc4ba 60%,#8e857b);overflow:hidden}
.video .vtitle{left:42px;top:8px;background:#315b6e;color:var(--white);font-size:10px;padding:2px 4px}
.video .vfrom{left:42px;top:26px;color:var(--white);font-size:7px}
.video .vfrom span{background:#315b6e;padding:1px 3px}
.video .vthumb{left:6px;top:6px;width:30px;height:30px;background:#222}
.video .vside{right:8px;top:6px;display:flex;flex-direction:column;gap:4px;align-items:center;color:var(--white);font-size:5px}
.video .vside i{width:22px;height:18px;background:#333;display:block}
.video .vbar{left:6px;bottom:0;width:382px;height:22px;background:rgba(0,0,0,.6)}

/* footer */
.site-footer{left:0;top:983px;width:775px;height:217px;background:var(--black)}
.site-footer .brand{left:37px;top:12px}
.social{right:30px;top:17px;display:flex;align-items:center;gap:7px;color:var(--white);font-size:6px;line-height:7px}
.social .sq{width:14px;height:14px;background:var(--green)}
.social .dot{width:14px;height:14px;border-radius:50%;background:var(--white)}
.footer-rule{left:0;top:51px;width:775px;height:2px;background:var(--green)}
.footer-col{top:74px;font-size:6.5px;line-height:11px;color:var(--footer-text)}
.footer-col h5{font-weight:400;color:var(--green);font-size:6px;border-bottom:1px solid #555;padding-bottom:1px;margin-bottom:3px;width:56px}
.copyright{left:0;top:196px;width:775px;text-align:center;font-size:6px;color:var(--footer-text)}
</style>
</head>
<body>

<header class="site-header abs">
  <div class="brand abs"><span>Quellmont Haus</span><span class="mark"></span></div>
  <nav class="main-nav abs"><span>Home</span><span>Shop</span><span class="current">Blog</span><span>About us</span><span>Feedback</span><span>FAQ</span><span>Contact</span></nav>
  <div class="auth abs"><span class="login">LOG IN</span><span class="signup">SIGN UP</span></div>
</header>

<div class="toolbar abs">
  <div class="discuss abs"><span class="bubble"></span><span>Start a<br>Discussion</span></div>
  <div class="search abs"><span class="label">Search</span><span class="field">enter a keyword or topic</span><span class="go">GO</span></div>
</div>
<div class="side-head cat-head abs">CATEGORIES <span class="arrow">↓</span></div>

<aside>
  <div class="sidebar abs"></div>
  <div class="categories abs">
    <div class="group"><h4>New releases</h4><ul><li>Lorem</li><li>ipsum</li><li>dolor</li></ul></div>
    <div class="group"><h4>Tutorials</h4><ul><li>Lorem</li><li>ipsum</li><li>dolor</li></ul></div>
    <div class="group"><h4>Products</h4><ul><li>Lorem</li><li>ipsum</li><li>dolor</li></ul></div>
    <div class="group"><h4>VIP Members</h4><ul><li>Lorem</li><li>ipsum</li><li>dolor</li></ul></div>
    <div class="group"><h4>Super cool stuff</h4><ul><li>Lorem</li><li>ipsum</li><li>dolor</li></ul></div>
  </div>
  <div class="scroll abs"></div>
  <div class="side-head gallery-head abs">PHOTO GALLERY <span class="arrow">↓</span></div>
  <div class="gallery abs">
    <div class="thumb" role="img" aria-label="Gallery photo of a visitor" style="background:linear-gradient(#e9d7b8,#7a5a3a)"></div>
    <div class="thumb" role="img" aria-label="Gallery photo of vape gear" style="background:linear-gradient(#2e3540,#111)"></div>
    <div class="thumb" role="img" aria-label="Gallery portrait photo" style="background:linear-gradient(#777,#222)"></div>
    <div class="thumb" role="img" aria-label="Gallery world map graphic" style="background:linear-gradient(#e07a1f,#3a1a08)"></div>
    <div class="thumb" role="img" aria-label="Gallery photo of a product" style="background:linear-gradient(#f4f4f4,#3b6f9c)"></div>
    <div class="thumb" role="img" aria-label="Gallery colourful portrait artwork" style="background:linear-gradient(135deg,#2fa0d8,#e8b04a,#d04a3a)"></div>
  </div>
  <div class="divider-black abs"></div>
  <div class="side-head events-head abs">EVENTS <span class="arrow">↓</span></div>
  <div class="event-art abs" role="img" aria-label="Painted event poster artwork"></div>
</aside>

<main>
  <h1 class="welcome abs">WELCOME TO OUR BLOG</h1>
  <p class="welcome-sub abs">PLEASE READ OUR POSTING RULES</p>

  <!-- post 1 -->
  <div class="post-icon abs" style="top:135px"><svg width="22" height="22" viewBox="0 0 22 22"><path d="M4 18 L6 12 L15 3 L19 7 L10 16 Z M4 18 L10 16" fill="none" stroke="#fff" stroke-width="2"/></svg></div>
  <h2 class="post-title abs" style="top:135px">TITLE LOREM IPSUM</h2>
  <div class="post-meta abs" style="top:171px;height:82px">DATE<div class="date">SEP <b>19</b></div>2013<br>TAGS<div class="tags">ENTERTAINMENT<br>NEW PRODUCTS</div>COMMENTS<br>0</div>
  <div class="photo abs" style="left:120px;top:176px;width:275px;height:182px" role="img" aria-label="Photo of a man in a dark jacket holding an e-cigarette"></div>
  <p class="post-text abs" style="left:400px;top:176px;width:230px">Lorem ipsum dolor sit amet, dam illum minimum nam ut, at sed veri dmodum eloquentiam. Usu et utamur numquam bonorum. Usu cu democritum intellegebat, vis enim volutpat gubergren eu. Usmur numquam bonorum, at sed veri admodum eloquentiamac isu et utamur numquam bonorum, at sed veri admodum eloquentiamac isu et borem ipsum dolor sit amet, dam illum minimum nam ut, at sed veri dmodum eloquentiam. Usu et utamur numquam bonorum. Usu cu democritum intellegebat, vis enim. Volutpat gubergren eu. Usmur numquam bonorum, at sed veri admodum eloquentiamac isu et utamur numquam bonorum, at sed veri admodum eloquentiamac isu et Lorem ipsum dolor sit amet, dam illum minimum nam ut, at sed veri dmodum eloquentiam. Usu et utamur numquam bonorum. Usu cu democritum intellegebat, vis enim volutpat gubergren eu. Usmur numquam bonorum, at sed veri admodum eloquentiamac isu et utamur numquam bonorum.</p>
  <div class="actions abs" style="left:545px;top:361px">
    <div class="act"><div class="btn"><svg width="12" height="12" viewBox="0 0 12 12"><circle cx="3" cy="6" r="2" fill="#111"/><circle cx="9" cy="2.5" r="2" fill="#111"/><circle cx="9" cy="9.5" r="2" fill="#111"/><path d="M3 6 L9 2.5 M3 6 L9 9.5" stroke="#111"/></svg></div>SHARE</div>
    <div class="act"><div class="btn"><svg width="12" height="12" viewBox="0 0 12 12"><path d="M1 5h2v6H1z M4 11V5l3-4c1 0 1.5 1 1 2.5L7.5 5H11v2l-1.5 4z" fill="#111"/></svg></div>LIKE</div>
    <div class="act"><div class="btn"><svg width="12" height="12" viewBox="0 0 12 12"><ellipse cx="6" cy="5" rx="5" ry="4" fill="#111"/><path d="M3 8 L2 11 L6 8.5" fill="#111"/></svg></div>COMMENT</div>
  </div>
  <div class="rule abs" style="top:392px"></div>

  <!-- post 2 -->
  <div class="post-icon abs" style="top:422px"><svg width="20" height="20" viewBox="0 0 20 20"><rect x="4" y="3" width="12" height="15" fill="none" stroke="#fff" stroke-width="2"/><path d="M7 3v15" stroke="#fff" stroke-width="2"/></svg></div>
  <h2 class="post-title abs" style="top:422px">TITLE LOREM IPSUM</h2>
  <div class="post-meta abs" style="top:458px;height:70px">DATE<div class="date">SEP <b>14</b></div>2013<br>TAGS<div class="tags">VIP MEMBERS<br>NEW PRODUCTS</div>COMMENTS</div>
  <div class="photo abs" style="left:122px;top:460px;width:510px;height:183px;background:linear-gradient(90deg,#dfe3e6,#f4f4f4 45%,#c9a47a 70%,#efeae2)" role="img" aria-label="Photo of a woman holding an e-cigarette in a bright room"></div>
  <p class="post-text abs" style="left:126px;top:651px;width:506px;line-height:10px">Lorem ipsum dolor sit amet, dam illum minimum nam ut, at sed veri dmodum eloquentiam. Usu et utamur numquam bonorum. Usu cu democritum intellegebat, vis enim volutpat gubergren eu. Usmur numquam bonorum, at sed veri admodum eloquentiamac isu et utamur numquam bonorum, at sed veri admodum eloquentiamac isu et borem ipsum dolor sit amet, dam illum minimum nam ut, at sed veri dmodum eloquentiam. Usu et utamur numquam bonorum. Usu cu democritum intellegebat, vis enim volutpat gubergren eu. Usmur numquam bonorum, at sed veri admodum eloquentiamac isu et utamur numquam bonorum, at sed veri admodum eloquentiamac isu et utamur numquam bonorum.</p>
  <div class="actions abs" style="left:545px;top:714px">
    <div class="act"><div class="btn"><svg width="12" height="12" viewBox="0 0 12 12"><circle cx="3" cy="6" r="2" fill="#111"/><circle cx="9" cy="2.5" r="2" fill="#111"/><circle cx="9" cy="9.5" r="2" fill="#111"/><path d="M3 6 L9 2.5 M3 6 L9 9.5" stroke="#111"/></svg></div>SHARE</div>
    <div class="act"><div class="btn"><svg width="12" height="12" viewBox="0 0 12 12"><path d="M1 5h2v6H1z M4 11V5l3-4c1 0 1.5 1 1 2.5L7.5 5H11v2l-1.5 4z" fill="#111"/></svg></div>LIKE</div>
    <div class="act"><div class="btn"><svg width="12" height="12" viewBox="0 0 12 12"><ellipse cx="6" cy="5" rx="5" ry="4" fill="#111"/><path d="M3 8 L2 11 L6 8.5" fill="#111"/></svg></div>COMMENT</div>
  </div>
  <div class="rule abs" style="top:745px"></div>

  <!-- post 3 -->
  <div class="post-icon abs" style="top:776px"><svg width="20" height="20" viewBox="0 0 20 20"><rect x="2" y="3" width="16" height="14" rx="2" fill="none" stroke="#fff" stroke-width="2"/><path d="M8 7 L13 10 L8 13 Z" fill="#fff"/></svg></div>
  <h2 class="post-title abs" style="top:776px">TITLE LOREM IPSUM</h2>
  <div class="post-meta abs" style="top:812px;height:74px">DATE<div class="date">SEP <b>12</b></div>2013<br>TAGS<div class="tags">VIP MEMBERS<br>NEW PRODUCTS</div>COMMENTS</div>
  <div class="video abs" role="img" aria-label="Embedded clipora video player showing rows of products">
    <div class="vthumb abs"></div>
    <div class="vtitle abs">Title For Movie Goes Here</div>
    <div class="vfrom abs">from <span>Your Channel</span></div>
    <div class="vside abs"><i></i>LIKE<i></i>SHARE<i></i>EMBED</div>
    <div class="vbar abs"></div>
  </div>
</main>

<footer class="site-footer abs">
  <div class="brand abs"><span>Quellmont Haus</span><span class="mark"></span></div>
  <div class="social abs"><span class="sq"></span><span>Stay in touch,<br>socialize with us</span><span class="dot"></span><span class="dot"></span><span class="dot"></span></div>
  <div class="footer-rule abs"></div>
  <div class="footer-col abs" style="left:51px"><h5>LOCATION</h5>2840 Larkfield Row<br>First Level<br>Brennick 40217<br>USA</div>
  <div class="footer-col abs" style="left:148px"><h5>CONTACT</h5>Tel: 01-800-420-118<br>Fax: 01-800-420-119<br>Email: info@quellmonthaus</div>
  <div class="footer-col abs" style="left:255px"><h5>MY ACCOUNT</h5>Login<br>Returns &amp; Warranties<br>VIP Cards</div>
  <div class="footer-col abs" style="left:363px"><h5>LEGAL</h5>Terms<br>Privacy</div>
  <div class="footer-col abs" style="left:466px"><h5>HELP</h5>Product Guides<br>FAQ<br>Location</div>
  <div class="footer-col abs" style="left:568px"><h5>LINKS</h5>Resources<br>Category Links<br>External Directory</div>
  <div class="footer-col abs" style="left:670px"><h5>COMPANY INFO</h5>About Us<br>Quality Certificate<br>Services</div>
  <p class="copyright abs">Copyright © 2013 Quellmont Haus. All Rights Reserved.</p>
</footer>

</body>
</html>
```